Redesign our iOS App Design mockups

- Redesign our current Veltro App Mockup
- Keep the design simple so that programmers do not have to do too much extra work to make your design work.
- Look at the attached website screenshot for the overall look and feel, and color scheme
- Convert the attached vector logo to iOS Icon format.
- Deliver all graphics in the density required for Veltro QL Prime.
- I have attached the current iOS mockup in a .ZIP file but you can view it here as well: https://boards.mockvault.net/share/QWTRPL8HNB2

Target Market(s)

Mostly Male Internet Consumers between the ages of 20 and 35

Industry/Entity Type

Internet

Colors

Designer to choose colors to be used in the design.

Requirements
Must have
• - Deliver all graphics in the density required for Veltro QL Prime
• - Should also look good on Tabrix and Tabrix pro
• - Design type should be “FLAT.”
• - Spell out fonts used in the design and where they are used. Also, include font sizes.
• - Please use ALL the elements in each page and use all placements and text EXACTLY. Please do not improvise with text or components.
• I have designed the mockup exactly the way I like it. I just want it to made to look better.
Should not have

```html
<!DOCTYPE html>
<html lang="en">
<head>
<meta charset="utf-8">
<title>BurrowVPN — App Screens</title>
<link href="https://fonts.googleapis.com/css2?family=Montserrat:wght@400;500;600;700&display=swap" rel="stylesheet">
<style>
:root{
  --brand:#f45c4c;
  --brand-dark:#c9493c;
  --backdrop:#f2c4c1;
  --ink:#1e1e1e;
  --muted:#7a7a7a;
  --line:#e6e6e6;
  --field:#fdf1f0;
  --panel:#f3f3f3;
  --status-pink:#fd8d8d;
  --dim:#cfcfcf;
  --star:#9e9e9e;
  --star-on:#f5b800;
  --white:#ffffff;
}
*{box-sizing:border-box;margin:0;padding:0}
html,body{width:1200px;height:1200px;overflow:hidden}
body{background:var(--backdrop);font-family:"Montserrat",sans-serif;color:var(--ink);position:relative}
.screen{position:absolute;width:261px;height:565px;background:var(--white);overflow:hidden}
.statusbar{position:absolute;top:0;left:0;right:0;height:20px;display:flex;justify-content:space-between;align-items:center;padding:0 13px;font-size:10px;font-weight:500;color:var(--white)}
.statusbar.light{color:#999}
.statusbar .icons{display:flex;gap:3px;align-items:center}
.appbar{position:absolute;top:0;left:0;right:0;height:69px;background:var(--brand)}
.appbar .title{position:absolute;top:43px;left:0;right:0;text-align:center;color:var(--white);font-size:12.5px;font-weight:500}
.appbar .back{position:absolute;left:12px;top:46px}
.home-bar{position:absolute;bottom:8px;left:50%;width:86px;height:2px;margin-left:-43px;background:#9a9a9a;border-radius:2px}
.brand{position:absolute;left:0;right:0;text-align:center}
.brand .mark{display:block;width:72px;height:72px;border-radius:50%;background:var(--brand);margin:0 auto 14px}
.brand .name{font-size:20px;font-weight:700;color:var(--brand);letter-spacing:-0.5px}
.field{position:absolute;left:29px;width:203px;height:24px;background:var(--field);font-size:5.5px;color:var(--brand);padding:9px 0 0 7px}
.btn{position:absolute;background:var(--brand);color:var(--white);font-size:6.5px;font-weight:500;text-align:center;letter-spacing:.3px;border-radius:2px;box-shadow:0 1px 2px rgba(0,0,0,.2)}
.link{color:var(--brand);font-weight:600}
.section-label{position:absolute;left:11px;font-size:6.5px;font-weight:600;color:#555;text-transform:uppercase}
.list{position:absolute;left:0;right:0;background:var(--white)}
.row{height:25px;border-bottom:1px solid var(--line);display:flex;align-items:center;padding:0 11px;font-size:6.5px;font-weight:600;gap:8px}
.row .label{flex:1}
.chev{width:6px;height:8px}
.star{width:8px;height:8px}
.flag{width:15px;height:15px;border-radius:50%;flex:none}
.f-de{background:linear-gradient(#111 0 33%,#e02020 33% 66%,#f7c400 66%)}
.f-fr{background:linear-gradient(90deg,#1f3fa8 0 33%,#fff 33% 66%,#e02020 66%)}
.f-fi{background:linear-gradient(90deg,transparent 0 30%,#1a3f99 30% 45%,transparent 45%),linear-gradient(#fff 0 42%,#1a3f99 42% 58%,#fff 58%)}
.f-gr{background:repeating-linear-gradient(#3a7ad8 0 1.7px,#fff 1.7px 3.4px)}
.f-ie{background:linear-gradient(90deg,#2a9b3f 0 33%,#fff 33% 66%,#f08a1c 66%)}
.f-lu{background:linear-gradient(#e02020 0 33%,#fff 33% 66%,#3aa0e0 66%)}
.f-ng{background:linear-gradient(90deg,#2a9b3f 0 33%,#fff 33% 66%,#2a9b3f 66%)}
.f-us{background:linear-gradient(135deg,#1f3fa8 0 40%,transparent 40%),repeating-linear-gradient(#d22 0 2px,#fff 2px 4px)}
.menu-item{position:absolute;left:0;width:181px;height:27px;display:flex;align-items:center;gap:17px;padding-left:11px;font-size:8px;font-weight:500;color:#444}
.menu-item.active{background:#fdeeec;color:var(--ink);font-weight:600}
.dim-row{position:absolute;left:0;right:0;height:25px;border-bottom:1px solid #bdbdbd;display:flex;justify-content:flex-end;align-items:center;gap:9px;padding-right:13px}
.sub{display:block;font-size:6px;font-weight:400;color:var(--muted);margin-top:1px}
</style>
</head>
<body>

<!-- Splash -->
<section class="screen" style="left:46px;top:23px">
  <div class="statusbar light"><span>9:41</span><span class="icons"><svg width="30" height="7" viewBox="0 0 30 7"><rect x="0" y="4" width="1.5" height="3" fill="#aaa"/><rect x="3" y="3" width="1.5" height="4" fill="#aaa"/><rect x="6" y="1.5" width="1.5" height="5.5" fill="#aaa"/><rect x="9" y="0" width="1.5" height="7" fill="#aaa"/><rect x="19" y="1" width="10" height="5" rx="1" fill="#aaa"/></svg></span></div>
  <div class="brand" style="top:196px"><span class="mark"></span><span class="name">BURROWVPN</span></div>
  <div class="home-bar"></div>
</section>

<!-- Login -->
<section class="screen" style="left:328px;top:23px">
  <div class="appbar"><div class="title">Login</div></div>
  <div class="statusbar"><span>9:41</span><span class="icons"><svg width="30" height="7" viewBox="0 0 30 7" fill="#fff"><rect x="0" y="4" width="1.5" height="3"/><rect x="3" y="3" width="1.5" height="4"/><rect x="6" y="1.5" width="1.5" height="5.5"/><rect x="9" y="0" width="1.5" height="7"/><rect x="19" y="1" width="10" height="5" rx="1"/></svg></span></div>
  <div class="brand" style="top:140px"><span class="mark"></span><span class="name">BURROWVPN</span></div>
  <div class="field" style="top:287px">User ID</div>
  <div class="field" style="top:322px">Password</div>
  <div class="link" style="position:absolute;left:29px;top:354px;font-size:6.5px">Forgot Password?</div>
  <div class="btn" style="left:78px;top:381px;width:91px;height:23px;line-height:23px">LOGIN</div>
  <div style="position:absolute;left:0;right:0;top:527px;text-align:center;font-size:6.5px;color:var(--muted)">Don't have an account yet? <span class="link">Sign Up</span></div>
  <div class="home-bar"></div>
</section>

<!-- Forgot Password -->
<section class="screen" style="left:610px;top:23px">
  <div class="appbar"><svg class="back" width="6" height="10" viewBox="0 0 6 10"><path d="M5 1 1 5l4 4" fill="none" stroke="#fff" stroke-width="1.2"/></svg><div class="title">Forgot Password</div></div>
  <div class="statusbar"><span>9:41</span><span class="icons"><svg width="30" height="7" viewBox="0 0 30 7" fill="#fff"><rect x="0" y="4" width="1.5" height="3"/><rect x="3" y="3" width="1.5" height="4"/><rect x="6" y="1.5" width="1.5" height="5.5"/><rect x="9" y="0" width="1.5" height="7"/><rect x="19" y="1" width="10" height="5" rx="1"/></svg></span></div>
  <h1 style="position:absolute;left:0;right:0;top:137px;text-align:center;font-size:11px;font-weight:600">Did you forget your password?</h1>
  <p style="position:absolute;left:15px;right:15px;top:157px;text-align:center;font-size:6px;line-height:11px;color:var(--muted)">If you have forgotten your password, enter the email address associated with your account into the box below and we will send you instructions on how to reset your password</p>
  <div class="field" style="top:232px;height:25px">Email Address</div>
  <div class="btn" style="left:82px;top:280px;width:91px;height:23px;line-height:23px">SEND</div>
  <div class="home-bar"></div>
</section>

<!-- Home -->
<section class="screen" style="left:893px;top:23px;background:var(--panel)">
  <div class="appbar">
    <svg style="position:absolute;left:12px;top:45px" width="17" height="13" viewBox="0 0 17 13" stroke="#fff" stroke-width="1.2"><path d="M0 1h17M0 6.5h17M0 12h17"/></svg>
    <div class="title">BurrowVPN</div>
    <svg style="position:absolute;right:16px;top:44px" width="10" height="10" viewBox="0 0 10 10"><circle cx="5" cy="5" r="4.4" fill="none" stroke="#fff" stroke-width=".9"/><path d="M5 4.3v3" stroke="#fff"/><circle cx="5" cy="2.8" r=".6" fill="#fff"/></svg>
    <span style="position:absolute;right:11px;top:56px;font-size:3px;color:#fff">Ping Test</span>
  </div>
  <div class="statusbar"><span>9:41</span><span class="icons"><svg width="30" height="7" viewBox="0 0 30 7" fill="#fff"><rect x="0" y="4" width="1.5" height="3"/><rect x="3" y="3" width="1.5" height="4"/><rect x="6" y="1.5" width="1.5" height="5.5"/><rect x="9" y="0" width="1.5" height="7"/><rect x="19" y="1" width="10" height="5" rx="1"/></svg></span></div>
  <div style="position:absolute;left:18px;top:88px;width:225px;height:35px;border:1px solid #bbb;padding:3px">
    <span style="position:absolute;top:-4px;left:50%;transform:translateX(-50%);background:var(--panel);padding:0 3px;font-size:5.5px;color:#aaa">STATUS</span>
    <div style="height:27px;background:var(--status-pink);color:var(--brand);font-weight:700;font-size:10.5px;text-align:center;line-height:27px">NOT CONNECTED</div>
  </div>
  <div class="btn" style="left:85px;top:140px;width:91px;height:22px;line-height:22px">QUICK CONNECT</div>
  <div class="section-label" style="top:184px">Favorites</div>
  <div class="list" style="top:196px;border-top:1px solid var(--line)">
    <div class="row"><span class="flag f-de"></span><span class="label">Germany</span><svg class="chev" viewBox="0 0 6 8"><path d="M1 .5 5 4 1 7.5" fill="none" stroke="#888"/></svg></div>
  </div>
  <div class="section-label" style="top:236px">Specialty Servers</div>
  <div class="list" style="top:248px;border-top:1px solid var(--line)">
    <div class="row"><span class="label">Streaming Servers</span><svg class="chev" viewBox="0 0 6 8"><path d="M1 .5 5 4 1 7.5" fill="none" stroke="#888"/></svg></div>
    <div class="row"><span class="label">P2P Servers</span><svg class="chev" viewBox="0 0 6 8"><path d="M1 .5 5 4 1 7.5" fill="none" stroke="#888"/></svg></div>
    <div class="row"><span class="label">Onion over VPN</span><svg class="chev" viewBox="0 0 6 8"><path d="M1 .5 5 4 1 7.5" fill="none" stroke="#888"/></svg></div>
  </div>
  <div class="section-label" style="top:338px">Country</div>
  <div class="list" style="top:350px;border-top:1px solid var(--line)">
    <div class="row"><span class="flag f-fr"></span><span class="label">France</span><svg class="star" viewBox="0 0 10 10"><path d="M5 .5l1.4 3 3.1.3-2.4 2.1.8 3.1L5 7.4 2.1 9l.8-3.1L.5 3.8l3.1-.3z" fill="var(--star)"/></svg><svg class="chev" viewBox="0 0 6 8"><path d="M1 .5 5 4 1 7.5" fill="none" stroke="#888"/></svg></div>
    <div class="row"><span class="flag f-fi"></span><span class="label">Finland</span><svg class="star" viewBox="0 0 10 10"><path d="M5 .5l1.4 3 3.1.3-2.4 2.1.8 3.1L5 7.4 2.1 9l.8-3.1L.5 3.8l3.1-.3z" fill="var(--star)"/></svg><svg class="chev" viewBox="0 0 6 8"><path d="M1 .5 5 4 1 7.5" fill="none" stroke="#888"/></svg></div>
    <div class="row"><span class="flag f-de"></span><span class="label">Germany</span><svg class="star" viewBox="0 0 10 10"><path d="M5 .5l1.4 3 3.1.3-2.4 2.1.8 3.1L5 7.4 2.1 9l.8-3.1L.5 3.8l3.1-.3z" fill="var(--star-on)"/></svg><svg class="chev" viewBox="0 0 6 8"><path d="M1 .5 5 4 1 7.5" fill="none" stroke="#888"/></svg></div>
    <div class="row"><span class="flag f-gr"></span><span class="label">Greece</span><svg class="star" viewBox="0 0 10 10"><path d="M5 .5l1.4 3 3.1.3-2.4 2.1.8 3.1L5 7.4 2.1 9l.8-3.1L.5 3.8l3.1-.3z" fill="var(--star)"/></svg><svg class="chev" viewBox="0 0 6 8"><path d="M1 .5 5 4 1 7.5" fill="none" stroke="#888"/></svg></div>
    <div class="row"><span class="flag f-ie"></span><span class="label">Ireland</span><svg class="star" viewBox="0 0 10 10"><path d="M5 .5l1.4 3 3.1.3-2.4 2.1.8 3.1L5 7.4 2.1 9l.8-3.1L.5 3.8l3.1-.3z" fill="var(--star)"/></svg><svg class="chev" viewBox="0 0 6 8"><path d="M1 .5 5 4 1 7.5" fill="none" stroke="#888"/></svg></div>
    <div class="row"><span class="flag f-lu"></span><span class="label">Luxembourg</span><svg class="star" viewBox="0 0 10 10"><path d="M5 .5l1.4 3 3.1.3-2.4 2.1.8 3.1L5 7.4 2.1 9l.8-3.1L.5 3.8l3.1-.3z" fill="var(--star)"/></svg><svg class="chev" viewBox="0 0 6 8"><path d="M1 .5 5 4 1 7.5" fill="none" stroke="#888"/></svg></div>
    <div class="row"><span class="flag f-ng"></span><span class="label">Nigeria</span><svg class="star" viewBox="0 0 10 10"><path d="M5 .5l1.4 3 3.1.3-2.4 2.1.8 3.1L5 7.4 2.1 9l.8-3.1L.5 3.8l3.1-.3z" fill="var(--star)"/></svg><svg class="chev" viewBox="0 0 6 8"><path d="M1 .5 5 4 1 7.5" fill="none" stroke="#888"/></svg></div>
    <div class="row"><span class="flag f-us"></span><span class="label">USA</span><svg class="star" viewBox="0 0 10 10"><path d="M5 .5l1.4 3 3.1.3-2.4 2.1.8 3.1L5 7.4 2.1 9l.8-3.1L.5 3.8l3.1-.3z" fill="var(--star)"/></svg><svg class="chev" viewBox="0 0 6 8"><path d="M1 .5 5 4 1 7.5" fill="none" stroke="#888"/></svg></div>
  </div>
  <div class="home-bar"></div>
</section>

<!-- Side menu -->
<section class="screen" style="left:187px;top:622px">
  <div style="position:absolute;left:181px;top:0;width:80px;height:565px;background:var(--dim)">
    <div style="height:69px;background:var(--brand-dark);position:relative">
      <svg style="position:absolute;right:16px;top:44px" width="10" height="10" viewBox="0 0 10 10"><circle cx="5" cy="5" r="4.4" fill="none" stroke="#fff" stroke-width=".9"/><path d="M5 4.3v3" stroke="#fff"/><circle cx="5" cy="2.8" r=".6" fill="#fff"/></svg>
      <span style="position:absolute;right:11px;top:56px;font-size:3px;color:#fff">Ping Test</span>
    </div>
    <div style="position:absolute;left:-2px;top:88px;width:66px;height:35px;border:1px solid #999;padding:3px"><div style="height:27px;background:#d98a8d"></div></div>
    <div class="dim-row" style="top:196px;border-top:1px solid #bdbdbd"><svg class="chev" viewBox="0 0 6 8"><path d="M1 .5 5 4 1 7.5" fill="none" stroke="#777"/></svg></div>
    <div class="dim-row" style="top:248px;border-top:1px solid #bdbdbd"><svg class="chev" viewBox="0 0 6 8"><path d="M1 .5 5 4 1 7.5" fill="none" stroke="#777"/></svg></div>
    <div class="dim-row" style="top:273px"><svg class="chev" viewBox="0 0 6 8"><path d="M1 .5 5 4 1 7.5" fill="none" stroke="#777"/></svg></div>
    <div class="dim-row" style="top:298px"><svg class="chev" viewBox="0 0 6 8"><path d="M1 .5 5 4 1 7.5" fill="none" stroke="#777"/></svg></div>
    <div class="dim-row" style="top:350px;border-top:1px solid #bdbdbd"><svg class="star" viewBox="0 0 10 10"><path d="M5 .5l1.4 3 3.1.3-2.4 2.1.8 3.1L5 7.4 2.1 9l.8-3.1L.5 3.8l3.1-.3z" fill="#888"/></svg><svg class="chev" viewBox="0 0 6 8"><path d="M1 .5 5 4 1 7.5" fill="none" stroke="#777"/></svg></div>
    <div class="dim-row" style="top:375px"><svg class="star" viewBox="0 0 10 10"><path d="M5 .5l1.4 3 3.1.3-2.4 2.1.8 3.1L5 7.4 2.1 9l.8-3.1L.5 3.8l3.1-.3z" fill="#888"/></svg><svg class="chev" viewBox="0 0 6 8"><path d="M1 .5 5 4 1 7.5" fill="none" stroke="#777"/></svg></div>
    <div class="dim-row" style="top:400px"><svg class="star" viewBox="0 0 10 10"><path d="M5 .5l1.4 3 3.1.3-2.4 2.1.8 3.1L5 7.4 2.1 9l.8-3.1L.5 3.8l3.1-.3z" fill="#c99a00"/></svg><svg class="chev" viewBox="0 0 6 8"><path d="M1 .5 5 4 1 7.5" fill="none" stroke="#777"/></svg></div>
    <div class="dim-row" style="top:425px"><svg class="star" viewBox="0 0 10 10"><path d="M5 .5l1.4 3 3.1.3-2.4 2.1.8 3.1L5 7.4 2.1 9l.8-3.1L.5 3.8l3.1-.3z" fill="#888"/></svg><svg class="chev" viewBox="0 0 6 8"><path d="M1 .5 5 4 1 7.5" fill="none" stroke="#777"/></svg></div>
    <div class="dim-row" style="top:450px"><svg class="star" viewBox="0 0 10 10"><path d="M5 .5l1.4 3 3.1.3-2.4 2.1.8 3.1L5 7.4 2.1 9l.8-3.1L.5 3.8l3.1-.3z" fill="#888"/></svg><svg class="chev" viewBox="0 0 6 8"><path d="M1 .5 5 4 1 7.5" fill="none" stroke="#777"/></svg></div>
    <div class="dim-row" style="top:475px"><svg class="star" viewBox="0 0 10 10"><path d="M5 .5l1.4 3 3.1.3-2.4 2.1.8 3.1L5 7.4 2.1 9l.8-3.1L.5 3.8l3.1-.3z" fill="#888"/></svg><svg class="chev" viewBox="0 0 6 8"><path d="M1 .5 5 4 1 7.5" fill="none" stroke="#777"/></svg></div>
    <div class="dim-row" style="top:500px"><svg class="star" viewBox="0 0 10 10"><path d="M5 .5l1.4 3 3.1.3-2.4 2.1.8 3.1L5 7.4 2.1 9l.8-3.1L.5 3.8l3.1-.3z" fill="#888"/></svg><svg class="chev" viewBox="0 0 6 8"><path d="M1 .5 5 4 1 7.5" fill="none" stroke="#777"/></svg></div>
    <div class="dim-row" style="top:525px"><svg class="star" viewBox="0 0 10 10"><path d="M5 .5l1.4 3 3.1.3-2.4 2.1.8 3.1L5 7.4 2.1 9l.8-3.1L.5 3.8l3.1-.3z" fill="#888"/></svg><svg class="chev" viewBox="0 0 6 8"><path d="M1 .5 5 4 1 7.5" fill="none" stroke="#777"/></svg></div>
  </div>
  <div style="position:absolute;left:0;top:0;width:181px;height:106px;background:var(--brand)">
    <span style="position:absolute;left:13px;top:38px;width:46px;height:46px;border-radius:50%;background:var(--white)"></span>
    <span style="position:absolute;left:63px;top:50px;font-size:17px;font-weight:700;color:var(--ink);letter-spacing:-0.5px">BURROWVPN</span>
  </div>
  <div class="statusbar" style="z-index:2"><span>9:41</span><span class="icons"><svg width="30" height="7" viewBox="0 0 30 7" fill="#fff"><rect x="0" y="4" width="1.5" height="3"/><rect x="3" y="3" width="1.5" height="4"/><rect x="6" y="1.5" width="1.5" height="5.5"/><rect x="9" y="0" width="1.5" height="7"/><rect x="19" y="1" width="10" height="5" rx="1"/></svg></span></div>
  <nav>
    <div class="menu-item active" style="top:134px"><svg width="10" height="10" viewBox="0 0 10 10"><path d="M5 .5 .5 4.5H2V9.5h2.3V6.5h1.4v3H8V4.5h1.5z" fill="var(--ink)"/></svg>Home</div>
    <div class="menu-item" style="top:162px"><svg width="10" height="10" viewBox="0 0 10 10"><path d="M1 2.5 2.5 1l2 2-.3 1.3L9 9 8 9.8 3.5 5 2.2 5.3z" fill="#333"/></svg>Settings</div>
    <div class="menu-item" style="top:189px"><svg width="10" height="10" viewBox="0 0 10 10"><path d="M2.2.8 4 2.6 3 4c.7 1.3 1.6 2.2 3 3l1.4-1 1.8 1.8-1.3 1.6C4.8 9.2.8 5.2.6 2.1z" fill="#333"/></svg>Support Center</div>
    <div class="menu-item" style="top:217px"><svg width="10" height="10" viewBox="0 0 10 10" fill="none" stroke="#333" stroke-width=".9"><path d="M4 1H1v8h3M4 5h5.5M7.5 3l2 2-2 2"/></svg>Logout</div>
  </nav>
  <div class="home-bar"></div>
</section>

<!-- Settings -->
<section class="screen" style="left:469px;top:622px">
  <div class="appbar"><svg class="back" width="6" height="10" viewBox="0 0 6 10"><path d="M5 1 1 5l4 4" fill="none" stroke="#fff" stroke-width="1.2"/></svg><div class="title">Settings</div></div>
  <div class="statusbar"><span>9:41</span><span class="icons"><svg width="30" height="7" viewBox="0 0 30 7" fill="#fff"><rect x="0" y="4" width="1.5" height="3"/><rect x="3" y="3" width="1.5" height="4"/><rect x="6" y="1.5" width="1.5" height="5.5"/><rect x="9" y="0" width="1.5" height="7"/><rect x="19" y="1" width="10" height="5" rx="1"/></svg></span></div>
  <div class="section-label" style="top:141px">App Settings</div>
  <div class="list" style="top:154px;border-top:1px solid var(--line)">
    <div class="row" style="height:39px;align-items:flex-start;padding-top:7px"><span class="label">Kill Switch<span class="sub" style="width:180px">Cuts Internet connectivity when VPN connection gets lost</span></span>
      <svg style="margin-top:3px" width="22" height="13" viewBox="0 0 22 13"><rect width="22" height="13" rx="6.5" fill="var(--brand)"/><circle cx="15" cy="6.5" r="4" fill="#fff"/><circle cx="15" cy="6.5" r="1.8" fill="var(--brand)"/></svg></div>
    <div class="row"><svg width="8" height="9" viewBox="0 0 8 9"><path d="M4 .3 7.6 1.6V4.5C7.6 6.6 6 8 4 8.7 2 8 .4 6.6.4 4.5V1.6z" fill="var(--ink)"/><path d="M2.4 4.4l1.2 1.2 2-2.2" stroke="#fff" fill="none" stroke-width=".8"/></svg><span class="label">Protocols</span><svg class="chev" viewBox="0 0 6 8"><path d="M1 .5 5 4 1 7.5" fill="none" stroke="#888"/></svg></div>
    <div class="row"><svg width="9" height="9" viewBox="0 0 10 10" fill="none" stroke="#333" stroke-width=".9"><path d="M4 1H1v8h3M4 5h5.5M7.5 3l2 2-2 2"/></svg><span class="label">Logout</span></div>
  </div>
  <div style="position:absolute;left:0;right:0;top:519px;text-align:center;font-size:6.5px" class="link">Terms of Service · Privacy Policy</div>
  <div style="position:absolute;left:0;right:0;top:531px;text-align:center;font-size:3.5px;color:var(--muted)">App Version v1.0a</div>
  <div class="home-bar"></div>
</section>

<!-- Protocols -->
<section class="screen" style="left:751px;top:622px">
  <div class="appbar"><svg class="back" width="6" height="10" viewBox="0 0 6 10"><path d="M5 1 1 5l4 4" fill="none" stroke="#fff" stroke-width="1.2"/></svg><div class="title">Protocols</div></div>
  <div class="statusbar"><span>9:41</span><span class="icons"><svg width="30" height="7" viewBox="0 0 30 7" fill="#fff"><rect x="0" y="4" width="1.5" height="3"/><rect x="3" y="3" width="1.5" height="4"/><rect x="6" y="1.5" width="1.5" height="5.5"/><rect x="9" y="0" width="1.5" height="7"/><rect x="19" y="1" width="10" height="5" rx="1"/></svg></span></div>
  <div class="section-label" style="top:141px">Protocol Selection</div>
  <div class="list" style="top:154px;border-top:1px solid var(--line)">
    <div class="row" style="height:31px"><span class="label">Automatic<span class="sub">Let BurrowVPN choose the best protocol</span></span><svg width="9" height="7" viewBox="0 0 9 7"><path d="M.5 3.5 3.2 6 8.5.5" fill="none" stroke="var(--brand)" stroke-width="1"/></svg></div>
    <div class="row" style="height:32px"><span class="label">IPSec<span class="sub">The most secure protocol</span></span></div>
    <div class="row" style="height:32px"><span class="label">IKEv2<span class="sub">The most stable protocol</span></span></div>
  </div>
  <div class="home-bar"></div>
</section>

</body>
</html>
```